Wedding Planning and Event Planners website

I am driven by perfection of my occupation and i look forward to having an attractive and contemporary website for an event and wedding planning group. We are located in the United States and Canada and we offer our services only in these two countries. My website is for people who are planning events such Church programs, weddings, musical concerts, Picnic, etc. My website should have imaginary of events such as weddings, musical concerts and picnic, etc.. I don't have any reference website because i want all designers to be creative and unique. I prefer blue,red,green,yellow colors.

Industry/Entity Type

Wedding

Coding

Coded - Design and coding required

```html
<!DOCTYPE html>
<html lang="en">
<head>
<meta charset="utf-8">
<title>Marlowe Planners – Wedding &amp; Event Planning</title>
<link href="https://fonts.googleapis.com/css2?family=Raleway:wght@300;400;600;700&family=Open+Sans:wght@400;600;700&display=swap" rel="stylesheet">
<style>
:root{
  --blue:#2f9bdb;
  --blue-footer:#339fdf;
  --red:#d22a2a;
  --yellow:#e3d50c;
  --teal:#3dbfa7;
  --ink:#333;
  --muted:#777;
  --grey-bg:#efefef;
  --line:#e2e2e2;
  --white:#fff;
}
*{box-sizing:border-box;margin:0;padding:0}
html,body{width:1200px;height:2557px;overflow:hidden}
body{position:relative;background:var(--white);font-family:"Open Sans",Arial,sans-serif;color:var(--ink)}
.abs{position:absolute}
a{color:inherit;text-decoration:none}

/* header */
.site-header{top:0;left:0;width:1200px;height:89px;background:var(--white)}
.brand{left:99px;top:27px;font-family:"Raleway",sans-serif;font-weight:400;font-size:29px;color:#222;white-space:nowrap}
.nav-item{top:40px;font-family:"Raleway",sans-serif;font-size:11.5px;color:#444;text-transform:uppercase;white-space:nowrap}
.caret{display:inline-block;width:5px;height:5px;border-right:1.5px solid #555;border-bottom:1.5px solid #555;transform:rotate(45deg);margin-left:7px;position:relative;top:-3px}

/* hero */
.hero{top:89px;left:0;width:1200px;height:484px;background:
  radial-gradient(ellipse 150px 230px at 660px 330px,rgba(245,242,236,.95),rgba(245,242,236,0) 75%),
  radial-gradient(ellipse 120px 240px at 740px 280px,rgba(40,40,70,.9),rgba(40,40,70,0) 80%),
  radial-gradient(ellipse 260px 240px at 900px 150px,rgba(235,215,175,.8),rgba(235,215,175,0) 75%),
  radial-gradient(ellipse 300px 260px at 140px 120px,rgba(70,90,40,.7),rgba(70,90,40,0) 80%),
  linear-gradient(90deg,#3b3322 0%,#5e5236 25%,#9c8a66 55%,#b8a684 75%,#6e5f42 100%)}
.hero-shade{top:89px;left:0;width:560px;height:484px;background:linear-gradient(90deg,rgba(0,0,0,.35),rgba(0,0,0,0))}
.hero-title{left:0;width:572px;text-align:center;top:220px;font-family:"Raleway",sans-serif;font-weight:300;font-size:31px;color:#fff;letter-spacing:1px}
.hero-sub{left:86px;top:270px;width:400px;text-align:center;font-family:"Raleway",sans-serif;font-weight:700;font-size:16.5px;line-height:30px;color:#fff;text-transform:uppercase}
.hero-text{left:96px;top:336px;width:380px;text-align:center;font-size:12px;line-height:23px;color:#fff}
.btn-red{background:var(--red);color:#fff;font-family:"Raleway",sans-serif;font-weight:700;text-transform:uppercase;display:flex;align-items:center;justify-content:center}
.hero-btn{left:196px;top:402px;width:180px;height:45px;font-size:14px}
.hero-dots{left:571px;top:537px;display:flex;gap:7px}
.hero-dots i{width:9px;height:9px;border-radius:50%;background:rgba(255,255,255,.6)}
.hero-dots i:first-child{background:var(--blue)}

/* services strip */
.service-strip{top:573px;left:0;width:1200px;height:120px;border-bottom:1px solid var(--line)}
.service{top:598px;width:320px}
.service .icon{position:absolute;left:0;top:0;width:51px;height:51px;border-radius:50%}
.service h3{position:absolute;left:63px;top:6px;font-family:"Raleway",sans-serif;font-weight:700;font-size:12.5px;color:#444;text-transform:uppercase}
.service p{position:absolute;left:63px;top:28px;width:240px;font-size:11px;line-height:22px;color:var(--muted)}

/* welcome */
.section-title{font-family:"Raleway",sans-serif;font-weight:700;color:var(--blue);text-transform:uppercase;white-space:nowrap}
.welcome-title{top:746px;left:0;width:1200px;text-align:center;font-size:31px}
.welcome-text{top:794px;left:0;width:1200px;text-align:center;font-size:13.5px;color:#555}
.cat-card{width:309px;height:232px}
.cat-card .label{position:absolute;left:0;bottom:9px;width:196px;height:62px;padding:10px 0 0 21px;color:#fff;background:var(--blue)}
.cat-card .label.red{background:var(--red)}
.cat-card .label b{display:block;font-family:"Raleway",sans-serif;font-weight:700;font-size:14px;text-transform:uppercase}
.cat-card .label span{display:flex;align-items:center;gap:5px;font-size:11.5px;margin-top:5px}
.more-btn{left:489px;top:1409px;width:221px;height:49px;font-size:13.5px}

/* features */
.feature-frame{left:99px;top:1524px;width:378px;height:260px;border:1px solid #ddd;background:#fff;padding:8px}
.feature-frame div{width:100%;height:100%;background:
  radial-gradient(circle 60px at 110px 40px,rgba(255,190,140,.7),rgba(255,190,140,0)),
  radial-gradient(ellipse 60px 90px at 240px 170px,rgba(40,90,170,.9),rgba(40,90,170,0)),
  radial-gradient(ellipse 50px 90px at 170px 170px,rgba(200,160,110,.8),rgba(200,160,110,0)),
  radial-gradient(ellipse 40px 80px at 330px 170px,rgba(40,130,70,.8),rgba(40,130,70,0)),
  linear-gradient(135deg,#4a2030,#8a3040 40%,#3a3050 75%,#1e1a28)}
.feature-title{left:527px;top:1535px;font-size:23px}
.feature-text{left:527px;top:1575px;width:540px;font-size:11.5px;line-height:22.5px;color:var(--muted)}
.feature-list{left:530px;top:1683px;list-style:none;font-size:11px;font-weight:700;color:#444;white-space:nowrap}
.feature-list li{display:flex;align-items:center;gap:12px;height:33px}

/* grey band */
.info-band{left:0;top:1848px;width:1200px;height:389px;background:var(--grey-bg)}
.gallery-title{left:99px;top:1897px;font-size:20px}
.gallery-text{left:99px;top:1933px;font-size:11px;color:var(--muted)}
.gallery-grid{left:99px;top:1973px;width:383px;height:191px;display:grid;grid-template-columns:repeat(4,1fr);grid-template-rows:repeat(2,1fr);gap:2px}
.gallery-grid div{width:100%;height:100%}
.news-title{left:540px;top:1919px;font-size:20px}
.news-arrows{left:777px;top:1921px;font-size:15px;color:#aaa;letter-spacing:6px}
.news-thumb{left:540px;top:1973px;width:82px;height:77px;background:linear-gradient(180deg,#5f7d3a,#8a9a5a 45%,#4f7a2e 70%,#3d5a22)}
.news-head{left:645px;top:1970px;width:180px;font-family:"Raleway",sans-serif;font-weight:700;font-size:14px;line-height:22px;color:#444}
.news-date{left:645px;top:2025px;font-size:11px;color:var(--muted)}
.news-text{left:540px;top:2063px;width:290px;font-size:11px;line-height:22px;color:var(--muted)}
.package-photo{left:863px;top:1911px;width:237px;height:151px;background:
  radial-gradient(ellipse 50px 70px at 120px 90px,rgba(40,40,55,.85),rgba(40,40,55,0)),
  radial-gradient(ellipse 40px 50px at 190px 110px,rgba(240,235,220,.8),rgba(240,235,220,0)),
  linear-gradient(135deg,#6d7a48,#a89a74 50%,#56603c)}
.package-box{left:863px;top:2062px;width:237px;height:101px;background:var(--teal);padding:18px 0 0 20px;color:#fff}
.package-box h4{font-family:"Raleway",sans-serif;font-weight:700;font-size:16.5px;text-transform:uppercase}
.package-box p{font-size:11px;line-height:20px;margin-top:5px;width:205px}
.go-dot{display:inline-block;width:11px;height:11px;border-radius:50%;background:var(--yellow);vertical-align:middle;margin-left:6px}

/* footer */
.site-footer{left:0;top:2237px;width:1200px;height:264px;background:var(--blue-footer);color:#fff}
.footer-h{font-family:"Raleway",sans-serif;font-weight:700;font-size:16px;color:#fff}
.footer-small{font-size:11px;line-height:22px;color:#fff}
.email-input{left:99px;top:2345px;width:312px;height:34px;background:#fff;color:#666;font-size:11.5px;padding:9px 15px}
.sub-btn{left:99px;top:2396px;width:128px;height:37px;font-family:"Open Sans",sans-serif;font-size:11px;font-weight:700}
.footer-links{left:469px;top:2303px;list-style:none;font-size:11px;line-height:22px;color:#fff}
.contact-row{display:flex;align-items:center;gap:10px}
.social{left:891px;top:2327px;display:flex;gap:11px}
.social i{width:27px;height:27px;border-radius:50%;background:var(--yellow);box-shadow:inset 0 0 0 2px var(--yellow),inset 0 0 0 3.5px rgba(255,255,255,.75)}
.footer-brand{left:893px;top:2377px;font-family:"Raleway",sans-serif;font-weight:400;font-size:22px;color:#fff;white-space:nowrap}
.bottom-bar{left:0;top:2501px;width:1200px;height:56px;background:#fff;font-size:11px;color:#555;display:flex;align-items:center;justify-content:center}
.bottom-bar span{margin:0 14px}
</style>
</head>
<body>

<header class="abs site-header">
  <div class="abs brand">Marlowe Planners</div>
</header>
<nav>
  <span class="abs nav-item" style="left:423px">Home</span>
  <span class="abs nav-item" style="left:510px">About Us</span>
  <span class="abs nav-item" style="left:624px">Category<i class="caret"></i></span>
  <span class="abs nav-item" style="left:736px">Services<i class="caret"></i></span>
  <span class="abs nav-item" style="left:846px">Events</span>
  <span class="abs nav-item" style="left:944px">Blog</span>
  <span class="abs nav-item" style="left:1031px">Contact Us</span>
</nav>

<section class="abs hero" role="img" aria-label="Photo of a bride and groom embracing in front of a historic building"></section>
<div class="abs hero-shade"></div>
<h1 class="abs hero-title">MARLOWE PLANNERS</h1>
<p class="abs hero-sub">We are a wedding planning and event planning company</p>
<p class="abs hero-text">We help people who are planning events such Church programs, weddings, musical concerts, Picnic, etc.</p>
<a class="abs btn-red hero-btn">Subscribe Here</a>
<div class="abs hero-dots"><i></i><i></i><i></i><i></i></div>

<section class="abs service-strip"></section>
<div class="abs service" style="left:99px">
  <div class="icon" style="background:var(--red)">
    <svg width="51" height="51" viewBox="0 0 51 51"><circle cx="21" cy="27" r="7" fill="none" stroke="#fff" stroke-width="2.5"/><circle cx="30" cy="27" r="7" fill="none" stroke="#fff" stroke-width="2.5"/></svg>
  </div>
  <h3>Wedding Planning</h3>
  <p>Lorem Ipsum is simply dummy text of the printing and typesetting industry.</p>
</div>
<div class="abs service" style="left:452px">
  <div class="icon" style="background:var(--yellow)">
    <svg width="51" height="51" viewBox="0 0 51 51"><circle cx="25.5" cy="25.5" r="11" fill="none" stroke="#fff" stroke-width="2.5"/><circle cx="25.5" cy="25.5" r="4" fill="#fff"/></svg>
  </div>
  <h3>Corporate Events</h3>
  <p>Lorem Ipsum is simply dummy text of the printing and typesetting industry.</p>
</div>
<div class="abs service" style="left:805px">
  <div class="icon" style="background:var(--teal)">
    <svg width="51" height="51" viewBox="0 0 51 51"><path d="M17 15h8l-1 9a3 3 0 0 1-6 0z M26 15h8l-1 9a3 3 0 0 1-6 0z M21 27v9 M30 27v9 M18 36h6 M27 36h6" fill="none" stroke="#fff" stroke-width="2"/></svg>
  </div>
  <h3>Other Events</h3>
  <p>Lorem Ipsum is simply dummy text of the printing and typesetting industry.</p>
</div>

<h2 class="abs section-title welcome-title">Welcome to Marlowe Planners</h2>
<p class="abs welcome-text">We help people who are planning events such Church programs, weddings, musical concerts, Picnic, etc.</p>

<div class="abs cat-card" style="left:99px;top:864px;background:radial-gradient(ellipse 130px 150px at 155px 190px,rgba(235,215,190,.95),rgba(235,215,190,0) 80%),linear-gradient(180deg,#1f6fcf,#5ea0e6 45%,#b7a58c 80%,#6a5a48)" role="img" aria-label="Photo of a gothic cathedral under a blue sky">
  <div class="label red"><b>Church Programs</b><span>Click here for view details <svg width="10" height="10" viewBox="0 0 10 10"><circle cx="5" cy="5" r="5" fill="#fff"/><path d="M4 2.8 6.2 5 4 7.2" fill="none" stroke="#d22a2a" stroke-width="1.4"/></svg></span></div>
</div>
<div class="abs cat-card" style="left:447px;top:864px;background:radial-gradient(ellipse 90px 70px at 210px 120px,rgba(250,250,250,.95),rgba(250,250,250,0) 80%),radial-gradient(ellipse 50px 90px at 90px 110px,rgba(255,255,255,.9),rgba(255,255,255,0) 80%),radial-gradient(circle 30px at 150px 90px,rgba(230,110,150,.7),rgba(230,110,150,0)),linear-gradient(160deg,#5f7a58,#9aa892 45%,#5a5a52)" role="img" aria-label="Photo of a newlywed couple beside a decorated white wedding car">
  <div class="label"><b>Weddings</b><span>Click here for view details <svg width="10" height="10" viewBox="0 0 10 10"><circle cx="5" cy="5" r="5" fill="#fff"/><path d="M4 2.8 6.2 5 4 7.2" fill="none" stroke="#2f9bdb" stroke-width="1.4"/></svg></span></div>
</div>
<div class="abs cat-card" style="left:793px;top:864px;background:radial-gradient(circle 50px at 90px 40px,rgba(180,170,255,.9),rgba(180,170,255,0)),radial-gradient(circle 40px at 230px 30px,rgba(200,200,255,.8),rgba(200,200,255,0)),radial-gradient(ellipse 120px 60px at 150px 200px,rgba(40,80,200,.8),rgba(40,80,200,0)),linear-gradient(160deg,#1a1f6a,#2c36b0 45%,#0a0c30)" role="img" aria-label="Photo of a band performing on a stage with blue lights">
  <div class="label"><b>Musical Concerts</b><span>Click here for view details <svg width="10" height="10" viewBox="0 0 10 10"><circle cx="5" cy="5" r="5" fill="#fff"/><path d="M4 2.8 6.2 5 4 7.2" fill="none" stroke="#2f9bdb" stroke-width="1.4"/></svg></span></div>
</div>
<div class="abs cat-card" style="left:99px;top:1130px;background:radial-gradient(ellipse 70px 100px at 90px 100px,rgba(245,215,150,.95),rgba(245,215,150,0) 80%),radial-gradient(ellipse 90px 120px at 250px 170px,rgba(250,250,250,.9),rgba(250,250,250,0) 80%),linear-gradient(135deg,#a8705a,#d8b898 45%,#8a6a4e)" role="img" aria-label="Photo of a smiling couple on a picnic">
  <div class="label"><b>Picnic</b><span>Click here for view details <svg width="10" height="10" viewBox="0 0 10 10"><circle cx="5" cy="5" r="5" fill="#fff"/><path d="M4 2.8 6.2 5 4 7.2" fill="none" stroke="#2f9bdb" stroke-width="1.4"/></svg></span></div>
</div>
<div class="abs cat-card" style="left:447px;top:1130px;background:radial-gradient(circle 40px at 90px 90px,rgba(230,180,150,.8),rgba(230,180,150,0)),radial-gradient(circle 40px at 200px 120px,rgba(230,180,150,.75),rgba(230,180,150,0)),radial-gradient(circle 30px at 280px 40px,rgba(220,30,120,.8),rgba(220,30,120,0)),linear-gradient(135deg,#1e1430,#5a1e4a 45%,#1a2460)" role="img" aria-label="Photo of friends in party hats celebrating a birthday">
  <div class="label"><b>Birthdays Parties</b><span>Click here for view details <svg width="10" height="10" viewBox="0 0 10 10"><circle cx="5" cy="5" r="5" fill="#fff"/><path d="M4 2.8 6.2 5 4 7.2" fill="none" stroke="#2f9bdb" stroke-width="1.4"/></svg></span></div>
</div>
<div class="abs cat-card" style="left:793px;top:1130px;background:radial-gradient(ellipse 50px 100px at 110px 90px,rgba(20,20,30,.85),rgba(20,20,30,0) 80%),radial-gradient(ellipse 160px 60px at 200px 200px,rgba(200,150,130,.6),rgba(200,150,130,0)),linear-gradient(135deg,#6a2414,#b4502a 45%,#3a1810)" role="img" aria-label="Photo of a speaker addressing a conference audience">
  <div class="label"><b>Corporate Event</b><span>Click here for view details <svg width="10" height="10" viewBox="0 0 10 10"><circle cx="5" cy="5" r="5" fill="#fff"/><path d="M4 2.8 6.2 5 4 7.2" fill="none" stroke="#2f9bdb" stroke-width="1.4"/></svg></span></div>
</div>

<a class="abs btn-red more-btn">View More Category</a>

<div class="abs feature-frame"><div role="img" aria-label="Photo of guests dancing at a festive party"></div></div>
<h2 class="abs section-title feature-title">Features of Marlowe Planners</h2>
<p class="abs feature-text">Lorem Ipsum is simply dummy text of the printing and typesetting industry. Lorem Ipsum has been the industry's standard dummy text ever since the 1500s, when an unknown printer took a galley of type and scrambled it to make a type specimen book. It has survived not only five centuries, but also the leap into electronic typesetting, remaining essentially unchanged.</p>
<ul class="abs feature-list">
  <li><svg width="10" height="8" viewBox="0 0 10 8"><path d="M1 4l3 3 5-6" fill="none" stroke="#e3c10c" stroke-width="2"/></svg>Lorem Ipsum is simply dummy text of the printing and typesetting industry.</li>
  <li><svg width="10" height="8" viewBox="0 0 10 8"><path d="M1 4l3 3 5-6" fill="none" stroke="#e3c10c" stroke-width="2"/></svg>Lorem Ipsum is simply dummy text of the printing and typesetting industry text of the printing.</li>
  <li><svg width="10" height="8" viewBox="0 0 10 8"><path d="M1 4l3 3 5-6" fill="none" stroke="#e3c10c" stroke-width="2"/></svg>Lorem Ipsum is simply dummy text of the printing and typesetting industry.</li>
</ul>

<section class="abs info-band"></section>
<h2 class="abs section-title gallery-title">Photo Gallery</h2>
<p class="abs gallery-text">Lorem Ipsum is simply dummy text of the printing and typesetting...</p>
<div class="abs gallery-grid" role="img" aria-label="Gallery of wedding and event photos">
  <div style="background:linear-gradient(135deg,#6e6e6a,#c8c6c0 55%,#8a8a84)"></div>
  <div style="background:radial-gradient(circle 30px at 50% 45%,#f4f6ee,#9bb27a 70%,#c8cfc0)"></div>
  <div style="background:linear-gradient(180deg,#5fa6dc,#a8d0ee 55%,#e6d8b8)"></div>
  <div style="background:linear-gradient(135deg,#3e2a1c,#8a5a36 50%,#c8a070)"></div>
  <div style="background:linear-gradient(135deg,#2e3e6a,#7a8ab0 50%,#c06060)"></div>
  <div style="background:linear-gradient(135deg,#e8e4de,#9a8a80 50%,#2a2424)"></div>
  <div style="background:linear-gradient(135deg,#1e1a2e,#6a2a4a 50%,#d0a070)"></div>
  <div style="background:linear-gradient(135deg,#d8c8a8,#f0ece4 45%,#2a2a30)"></div>
</div>

<h2 class="abs section-title news-title">News &amp; Events</h2>
<div class="abs news-arrows">‹ ›</div>
<div class="abs news-thumb" role="img" aria-label="Photo of an outdoor event on a lawn"></div>
<h3 class="abs news-head">Lorem Ipsum is simply dummy text...</h3>
<p class="abs news-date">Posted on 27 March 2016</p>
<p class="abs news-text">Lorem Ipsum is simply dummy text of the printing and typesetting industry. Lorem Ipsum has been the industry's standard dummy text ever since the 1500s, when an unknown printer...</p>

<div class="abs package-photo" role="img" aria-label="Photo of a couple kissing outdoors"></div>
<div class="abs package-box">
  <h4>Honey Moon Package</h4>
  <p>Lorem Ipsum is simply dummy text of the printing and typesetting... <i class="go-dot"></i></p>
</div>

<footer class="abs site-footer"></footer>
<h3 class="abs footer-h" style="left:99px;top:2273px">Newsletter signup</h3>
<p class="abs footer-small" style="left:99px;top:2302px">Get our recent updates through your email id</p>
<div class="abs email-input">Enter your email id</div>
<a class="abs btn-red sub-btn">Subscribe Now</a>

<h3 class="abs footer-h" style="left:469px;top:2273px">Welcome</h3>
<ul class="abs footer-links">
  <li>Home</li><li>About Us</li><li>Services</li><li>Category</li><li>Gallery</li><li>Events</li><li>Contact Us</li>
</ul>

<h3 class="abs footer-h" style="left:630px;top:2273px">Contact Info</h3>
<div class="abs" style="left:630px;top:2302px;color:#fff;font-size:13px">Marlowe Planners</div>
<p class="abs footer-small" style="left:630px;top:2328px">120 Street name, City name,<br>Country name : 55501234</p>
<div class="abs footer-small contact-row" style="left:630px;top:2380px">
  <svg width="12" height="12" viewBox="0 0 12 12"><path d="M2 1l2.5 0 1 3-1.5 1a7 7 0 0 0 3 3l1-1.5 3 1V10a1 1 0 0 1-1 1A9 9 0 0 1 1 2a1 1 0 0 1 1-1z" fill="#e3d50c"/></svg>( 5550 ) 214 876</div>
<div class="abs footer-small contact-row" style="left:630px;top:2405px">
  <svg width="13" height="10" viewBox="0 0 13 10"><rect x=".75" y=".75" width="11.5" height="8.5" fill="none" stroke="#e3d50c" stroke-width="1.5"/><path d="M1 1l5.5 4.5L12 1" fill="none" stroke="#e3d50c" stroke-width="1.5"/></svg>info@marloweplanners.com</div>

<h3 class="abs footer-h" style="left:891px;top:2273px">Follow Us</h3>
<p class="abs footer-small" style="left:891px;top:2300px">Connect with our social network</p>
<div class="abs social" aria-label="Social network links"><i></i><i></i><i></i><i></i></div>
<div class="abs footer-brand">Marlowe Planners</div>

<div class="abs bottom-bar">
  <span>© 2016. Marlowe Planners. All rights reserved.</span><span>Terms &amp; Conditions</span>/<span>Privacy Policy</span>/<span>Disclaimer</span>
</div>

</body>
</html>
```